Wordpress website design for membership site

I need a wordpress website designed for a membership site specializing in member video recordings and storage. I need the site to be simplistic but fully functional. I want a minimalistic landing and member page. The member page needs to be able to showcase the members recorded videos amd utilize a GUI system of navigation utilizing graphical buttons. Member signup page needs to be fully functional to include email verification and password change/recovery functionality.

Coding

Coded - Design and coding required

Number of Pages Required

3 page

Font styles to use
Sans Serif

Colors

Designer to choose colors to be used in the design.

Requirements
Must have
• The project must incorporate the name TELQOR or TELQOR.example within the design.
Should not have
• Project should not use prepublished templates available online but should be unique in design and functionality.

```html
<!DOCTYPE html>
<html lang="en">
<head>
<meta charset="utf-8">
<title>TELQOR – Video Recordings &amp; Storage</title>
<link href="https://fonts.googleapis.com/css2?family=Jost:wght@300;400;500&family=Poppins:wght@400;500;600;700&display=swap" rel="stylesheet">
<style>
:root{
  --navy:#0e1a2b;
  --navy-deep:#070d17;
  --blue:#1780b8;
  --blue-dark:#0f6799;
  --blue-light:#2aa0d8;
  --orange:#e8581f;
  --orange-dark:#c0361a;
  --orange-light:#f47b2b;
  --red:#cf2f1c;
  --grey-bg:#ebebeb;
  --line:#e2e2e2;
  --text:#222;
  --muted:#555;
  --white:#fff;
}
*{margin:0;padding:0;box-sizing:border-box}
html,body{width:1200px;height:4478px;overflow:hidden}
body{font-family:"Poppins",sans-serif;color:var(--text);background:var(--white);position:relative}
section,header,footer{position:absolute;left:0;width:1200px}
.heading{font-family:"Jost",sans-serif;font-weight:400;font-size:44px;text-align:center;color:#1b1b1b}

/* Hero */
.hero{top:0;height:780px;overflow:hidden}
.hero-photo{position:absolute;inset:0;background:radial-gradient(ellipse at 50% 30%,#2a3a50 0%,#141f30 45%,var(--navy-deep) 100%)}
.hero-shape{position:absolute;left:0;top:0}
.brand{position:absolute;left:146px;top:34px;color:var(--white)}
.brand-name{font-weight:700;font-size:40px;letter-spacing:1px;line-height:1}
.brand-tag{font-size:11px;font-weight:500;width:180px;text-align:center;margin-top:10px;line-height:1.45}
.call{position:absolute;left:588px;top:37px;color:var(--white);font-size:18px;font-weight:500;display:flex;align-items:center;gap:10px}
.call svg{width:32px;height:32px}
.member-btn{position:absolute;left:894px;top:30px;width:164px;height:44px;border:2px solid var(--white);border-radius:22px;color:var(--white);font-size:15px;font-weight:500;display:flex;align-items:center;justify-content:center}
.nav{position:absolute;left:480px;top:100px;display:flex;gap:28px;color:var(--white);font-size:16px;font-weight:500}
.hero-title{position:absolute;left:146px;top:280px;color:var(--white);font-weight:500;font-size:58px;line-height:1}
.hero-sub{position:absolute;left:146px;top:355px;color:var(--white);font-family:"Jost",sans-serif;font-size:32px}
.btn-blue{position:absolute;left:146px;top:420px;width:196px;height:44px;border-radius:22px;background:var(--blue);color:var(--white);font-weight:600;font-size:17px;display:flex;align-items:center;justify-content:center}
.dots{position:absolute;left:150px;top:502px;display:flex;gap:17px}
.dots span{width:16px;height:16px;border:2px solid var(--white);border-radius:50%}
.dots span:first-child{background:rgba(255,255,255,.4)}

/* Services */
.services{top:780px;height:790px}
.services .heading{margin-top:30px}
.svc{position:absolute;width:260px}
.svc-icon{width:96px;height:96px;border-radius:50%;background:var(--blue);display:flex;align-items:center;justify-content:center}
.svc-icon svg{width:50px;height:50px}
.svc h3{font-size:16.5px;font-weight:700;line-height:1.55;margin-top:20px;text-transform:uppercase}
.svc p{font-size:12.5px;line-height:1.9;color:var(--muted);margin-top:14px}

/* Preserve band */
.preserve{top:1560px;height:590px}
.preserve-bg{position:absolute;left:0;top:0}
.preserve h2{position:absolute;left:146px;top:145px;color:var(--white);font-family:"Jost",sans-serif;font-weight:400;font-size:44px;line-height:1.28}
.preserve p{position:absolute;left:146px;top:270px;width:440px;color:#d6ecf8;font-size:13px;line-height:2}
.btn-outline{position:absolute;left:146px;top:442px;width:148px;height:40px;border:2px solid var(--white);border-radius:20px;color:var(--white);font-size:16px;display:flex;align-items:center;justify-content:center}
.frame{position:absolute;left:606px;top:140px;width:395px;height:300px;border:2px solid var(--white)}
.preserve-photo{position:absolute;left:628px;top:162px;width:422px;height:310px;background:linear-gradient(135deg,#e9f1fb 0%,#b9cde4 50%,#7b93b3 100%);border:1px solid #fff}

/* Pricing */
.pricing{top:2143px;height:827px;background:var(--grey-bg)}
.pricing .heading{margin-top:70px}
.plan{position:absolute;background:var(--white);border:1px solid #f2cdb4;text-align:center}
.plan.featured{border:1px solid #ddd;box-shadow:0 4px 14px rgba(0,0,0,.18);z-index:2}
.price{position:absolute;left:50%;transform:translateX(-50%);width:116px;height:116px;border-radius:50%;background:radial-gradient(circle at 40% 35%,var(--orange-light),var(--red) 75%);color:var(--white);display:flex;flex-direction:column;align-items:center;justify-content:center;box-shadow:0 0 0 6px rgba(232,88,31,.15)}
.price b{font-size:32px;font-weight:600;line-height:1;letter-spacing:-1px}
.price b small{font-size:16px}
.price span{font-size:10px;margin-top:4px}
.plan h3{font-family:"Jost",sans-serif;font-weight:500;font-size:25px;margin-top:104px}
.plan ul{list-style:none;margin-top:14px}
.plan li{font-size:12.5px;height:40px;line-height:40px;border-top:1px solid var(--line)}
.plan li:last-child{border-bottom:1px solid var(--line)}
.sub-btn{display:inline-flex;align-items:center;justify-content:center;width:112px;height:36px;background:var(--orange);color:var(--white);font-size:13px;font-weight:600;margin-top:30px}
.featured .sub-btn{background:var(--red)}

/* News */
.news{top:2970px;height:642px}
.news .heading{margin-top:70px}
.card{position:absolute;top:179px;width:290px;height:358px;border:1px solid #ddd;background:var(--white)}
.card-photo{height:185px;background:linear-gradient(135deg,#f3d6a6 0%,#a88a6a 50%,#3e3a38 100%)}
.card h3{font-family:"Jost",sans-serif;font-weight:400;font-size:20px;margin:22px 0 0 18px}
.card .date{color:var(--blue);font-size:11px;font-weight:700;margin:10px 0 0 18px;display:flex;align-items:center;gap:8px}
.card p{font-size:11.5px;line-height:1.75;color:var(--muted);margin:10px 18px 0}

/* Testimonial */
.testimonial{top:3600px;height:600px}
.testimonial-bg{position:absolute;left:0;top:0}
.avatar{position:absolute;left:547px;top:138px;width:106px;height:106px;border-radius:50%;background:linear-gradient(160deg,#9fb1c4,#31425a);border:4px solid #f4b59b}
.quote{position:absolute;top:148px;color:var(--white);font-family:"Jost",sans-serif;font-size:64px;line-height:1}
.testimonial h2{position:absolute;top:268px;width:100%;text-align:center;color:var(--white);font-family:"Jost",sans-serif;font-weight:400;font-size:34px}
.testimonial p{position:absolute;left:150px;top:330px;width:900px;text-align:center;color:#ffe4d6;font-size:13.5px;line-height:2.2}
.author{position:absolute;top:440px;width:100%;text-align:center;color:var(--white);font-size:15px;font-weight:600;font-style:italic}

/* Footer */
.footer{top:4200px;height:278px;text-align:center}
.social{position:absolute;left:535px;top:55px;display:flex;gap:12px}
.social span{width:38px;height:38px;border-radius:50%;border:2px solid #333}
.foot-nav{position:absolute;top:130px;width:100%;font-size:16px;color:#222;word-spacing:2px}
.foot-nav i{font-style:normal;margin:0 12px}
.copy{position:absolute;top:178px;width:100%;font-size:15px;color:#333}
</style>
</head>
<body>

<header class="hero">
  <div class="hero-photo" role="img" aria-label="Photo of a man working on a laptop in a dark server room"></div>
  <svg class="hero-shape" width="1200" height="780" viewBox="0 0 1200 780" aria-hidden="true">
    <polygon points="0,695 340,710 0,745" fill="var(--blue-dark)"/>
    <polygon points="0,745 340,710 1200,750 1200,780 0,780" fill="var(--white)"/>
    <polygon points="0,690 360,705 0,760" fill="var(--blue)"/>
    <polygon points="0,760 360,705 1200,755 1200,780 0,780" fill="var(--white)"/>
  </svg>
  <div class="brand">
    <div class="brand-name">TELQOR</div>
    <div class="brand-tag">PRESERVING YOU FOR FUTURE GENERATIONS</div>
  </div>
  <div class="call">
    <svg viewBox="0 0 32 32"><circle cx="16" cy="16" r="15" fill="var(--white)"/><path d="M11 9c1-1 2 0 3 2s0 2-1 3c1 2 3 4 5 5 1-1 1-2 3-1s3 2 2 3c-1 2-3 3-5 2-4-2-7-5-8-9 0-2 0-4 1-5z" fill="var(--navy)"/></svg>
    Call Us : (555) 0147 2290
  </div>
  <div class="member-btn">MEMBERSHIP</div>
  <nav class="nav"><span>HOME</span><span>WHAT WE DO</span><span>SERVICES</span><span>BLOG</span><span>ABOUT</span><span>CONTACT US</span></nav>
  <h1 class="hero-title">TELQOR</h1>
  <div class="hero-sub">Video Recordings &amp; Storage</div>
  <div class="btn-blue">LEARN MORE</div>
  <div class="dots"><span></span><span></span><span></span></div>
</header>

<section class="services">
  <h2 class="heading">What we do?</h2>
  <div class="svc" style="left:146px;top:155px">
    <div class="svc-icon"><svg viewBox="0 0 50 50" fill="none" stroke="#fff" stroke-width="2"><rect x="12" y="8" width="26" height="34" rx="2"/><polygon points="21,19 30,25 21,31" fill="#fff"/></svg></div>
    <h3>Quis autem vel eum iure reprehenderit qui</h3>
    <p>Lorem ipsum dolor sit amet, consectetur adipiscing elit, sed do eiusmod tempor incididunt ut labore et dolore</p>
  </div>
  <div class="svc" style="left:463px;top:155px">
    <div class="svc-icon"><svg viewBox="0 0 50 50" fill="none" stroke="#fff" stroke-width="2"><rect x="8" y="10" width="34" height="24" rx="2"/><path d="M18 40h14M25 34v6M14 16h10v12H14zM28 18h8M28 23h8M28 28h8"/></svg></div>
    <h3>Quis autem vel eum iure reprehenderit qui</h3>
    <p>Lorem ipsum dolor sit amet, consectetur adipiscing elit, sed do eiusmod tempor incididunt ut labore et dolore</p>
  </div>
  <div class="svc" style="left:782px;top:155px">
    <div class="svc-icon"><svg viewBox="0 0 50 50" fill="none" stroke="#fff" stroke-width="2"><rect x="10" y="10" width="12" height="8"/><rect x="10" y="21" width="12" height="8"/><rect x="10" y="32" width="12" height="8"/><path d="M22 25h8M30 14v22M30 14h8M30 36h8"/></svg></div>
    <h3>Quis autem vel eum iure reprehenderit qui</h3>
    <p>Lorem ipsum dolor sit amet, consectetur adipiscing elit, sed do eiusmod tempor incididunt ut labore et dolore</p>
  </div>
  <div class="svc" style="left:146px;top:432px">
    <div class="svc-icon"><svg viewBox="0 0 50 50" fill="none" stroke="#fff" stroke-width="2"><rect x="19" y="8" width="12" height="10"/><rect x="8" y="32" width="10" height="10"/><rect x="20" y="32" width="10" height="10"/><rect x="32" y="32" width="10" height="10"/><path d="M25 18v7M13 32v-7h24v7M25 25v7"/></svg></div>
    <h3>Integrated digital brand campaigns</h3>
    <p>Lorem ipsum dolor sit amet, consectetur adipiscing elit, sed do eiusmod tempor incididunt ut labore et dolore</p>
  </div>
  <div class="svc" style="left:463px;top:432px">
    <div class="svc-icon"><svg viewBox="0 0 50 50" fill="none" stroke="#fff" stroke-width="2"><rect x="10" y="12" width="30" height="28" rx="2"/><path d="M10 20h30M17 8v8M33 8v8M16 26h4M23 26h4M30 26h4M16 33h4M23 33h4M30 33h4"/></svg></div>
    <h3>Sports and events fan engagement strategy</h3>
    <p>Lorem ipsum dolor sit amet, consectetur adipiscing elit, sed do eiusmod tempor incididunt ut labore et dolore</p>
  </div>
  <div class="svc" style="left:782px;top:432px">
    <div class="svc-icon"><svg viewBox="0 0 50 50" fill="none" stroke="#fff" stroke-width="2"><rect x="9" y="10" width="32" height="24" rx="2"/><path d="M19 40h12M25 34v6M14 16h22M14 22h22M14 28h14"/></svg></div>
    <h3>Quis autem vel eum iure reprehenderit qui</h3>
    <p>Lorem ipsum dolor sit amet, consectetur adipiscing elit, sed do eiusmod tempor incididunt ut labore et dolore</p>
  </div>
</section>

<section class="preserve">
  <svg class="preserve-bg" width="1200" height="590" viewBox="0 0 1200 590" aria-hidden="true">
    <polygon points="0,5 1200,55 1200,590 0,590" fill="var(--blue)"/>
    <polygon points="0,5 560,30 0,60" fill="var(--blue-dark)"/>
    <polygon points="560,30 1200,55 1200,80" fill="var(--blue-light)" opacity=".6"/>
  </svg>
  <h2>Preserving You For<br>Future Generations</h2>
  <p>Sed ut perspiciatis unde omnis iste natus error sit voluptatem accusantium doloremque laudantium, totam rem aperiam, eaque ipsa quae ab illo inventore veritatis et quasi architecto beatae vitae dicta sunt explicabo. Nemo enim ipsam voluptatem quia voluptas sit aspernatur aut odit aut fugit</p>
  <div class="btn-outline">Learn More</div>
  <div class="frame"></div>
  <div class="preserve-photo" role="img" aria-label="Photo of a hand using a laptop with floating video playback graphics"></div>
</section>

<section class="pricing">
  <h2 class="heading">Our Pricing</h2>
  <div class="plan" style="left:161px;top:260px;width:281px;height:433px">
    <div class="price" style="top:-75px"><b><small>$</small>999</b><span>per annum</span></div>
    <h3>Silver Package</h3>
    <ul><li>Monday And Wednesday</li><li>Sed Ut Perspiciatis Unde Omnis</li><li>Duis Aute Irure Dolor In</li><li>Additional Users</li><li>Nemo Enim Ipsam Voluptatem</li></ul>
    <div class="sub-btn">SUBSCRIBE</div>
  </div>
  <div class="plan featured" style="left:442px;top:240px;width:319px;height:477px">
    <div class="price" style="top:-65px"><b><small>$</small>1222</b><span>per annum</span></div>
    <h3>Gold Package</h3>
    <ul><li>Monday And Wednesday</li><li>Sed Ut Perspiciatis Unde Omnis</li><li>Duis Aute Irure Dolor In</li><li>Additional Users</li><li>Nemo Enim Ipsam Voluptatem</li></ul>
    <div style="background:#ededed;height:100px;margin-top:0;padding-top:0"><div class="sub-btn">SUBSCRIBE</div></div>
  </div>
  <div class="plan" style="left:761px;top:260px;width:278px;height:433px">
    <div class="price" style="top:-75px"><b><small>$</small>2,500</b><span>per annum</span></div>
    <h3>Platinum Package</h3>
    <ul><li>Monday And Wednesday</li><li>Sed Ut Perspiciatis Unde Omnis</li><li>Duis Aute Irure Dolor In</li><li>Additional Users</li><li>Nemo Enim Ipsam Voluptatem</li></ul>
    <div class="sub-btn">SUBSCRIBE</div>
  </div>
</section>

<section class="news">
  <h2 class="heading">Latest News</h2>
  <article class="card" style="left:144px">
    <div class="card-photo" role="img" aria-label="Photo of people reviewing documents at a desk"></div>
    <h3>Quis autem vel eum iure</h3>
    <div class="date"><svg width="11" height="11" viewBox="0 0 11 11"><rect x="0.5" y="1.5" width="10" height="9" fill="none" stroke="var(--blue)"/><rect x="0.5" y="1.5" width="10" height="3" fill="var(--blue)"/></svg>OCTOBER 17, 2019</div>
    <p>Sed ut perspiciatis unde omnis iste natus error sit voluptatem accusantium dolorque lauda, totam rem operiam</p>
  </article>
  <article class="card" style="left:455px">
    <div class="card-photo" role="img" aria-label="Photo of a laptop and paperwork on a desk"></div>
    <h3>Quis autem vel eum iure</h3>
    <div class="date"><svg width="11" height="11" viewBox="0 0 11 11"><rect x="0.5" y="1.5" width="10" height="9" fill="none" stroke="var(--blue)"/><rect x="0.5" y="1.5" width="10" height="3" fill="var(--blue)"/></svg>OCTOBER 17, 2019</div>
    <p>Sed ut perspiciatis unde omnis iste natus error sit voluptatem accusantium dolorque lauda, totam rem operiam</p>
  </article>
  <article class="card" style="left:767px">
    <div class="card-photo" role="img" aria-label="Photo of a team working together on laptops"></div>
    <h3>Quis autem vel eum iure</h3>
    <div class="date"><svg width="11" height="11" viewBox="0 0 11 11"><rect x="0.5" y="1.5" width="10" height="9" fill="none" stroke="var(--blue)"/><rect x="0.5" y="1.5" width="10" height="3" fill="var(--blue)"/></svg>OCTOBER 17, 2019</div>
    <p>Sed ut perspiciatis unde omnis iste natus error sit voluptatem accusantium dolorque lauda, totam rem operiam</p>
  </article>
</section>

<section class="testimonial">
  <svg class="testimonial-bg" width="1200" height="600" viewBox="0 0 1200 600" aria-hidden="true">
    <defs><linearGradient id="warm" x1="0" y1="0" x2="0" y2="1"><stop offset="0" stop-color="var(--orange)"/><stop offset="1" stop-color="var(--orange-dark)"/></linearGradient></defs>
    <polygon points="0,12 1200,0 1200,560 0,510" fill="url(#warm)"/>
    <polygon points="0,12 380,8 0,60" fill="var(--orange-light)"/>
    <polygon points="780,40 1200,10 1200,70" fill="var(--red)"/>
    <polygon points="0,510 700,540 0,585" fill="var(--orange-light)"/>
    <polygon points="0,585 700,540 1200,560 1200,600 0,600" fill="var(--white)"/>
  </svg>
  <div class="quote" style="left:488px">“</div>
  <div class="avatar" role="img" aria-label="Client portrait photo"></div>
  <div class="quote" style="left:670px">”</div>
  <h2>Client Testimonials</h2>
  <p>Sed ut perspiciatis unde omnis iste natus error sit voluptatem accusantium doloremque laudantium, totam rem aperiam, eaque ipsa quae ab illo inventore veritatis et quasi architecto beatae vitae dicta sunt explicabo. Nemo enim ipsam voluptatem quia voluptas sit aspernatur aut odit aut fugit Sed ut perspiciatis unde omnis iste natus error sit voluptatem</p>
  <div class="author">— Blandit Lectus</div>
</section>

<footer class="footer">
  <div class="social" aria-label="Social links"><span></span><span></span><span></span></div>
  <div class="foot-nav">Home<i>|</i>About Us<i>|</i>Services<i>|</i>What's New<i>|</i>Blog<i>|</i>Contact</div>
  <div class="copy">Copyright © TELQOR 2019. All rights reserved.</div>
</footer>

</body>
</html>
```